sharing light. a peaceful way of living.

adding value to ones circumstance through the teachings of neutralization. quote for back of card: "and then it happens... One day you wake up and you're in this place. You are in this place where everything is right. Your heart is calm. Your soul is lit. Your thoughts are positive. Your vision is clear. Your faith is stronger than ever. And you are at peace. At peace with where you have been. At peace with what you've been through. And at peace with where you're headed." -unknown

Target Market(s)

spiritual, awakening, inspiration, motivation, gratefulness, oneness, peace, positive mindset,

Contact Information for Business Card

front: one line message from quote

Logo Text

up to suggestions

Font styles to use
Serif
Sans Serif
Script

Colors

Designer to choose colors to be used in the design.

Requirements
Must have
• entire quote on one side of card
Nice to have
• simple, and to the point
Should not have
• elaborated designs

```html
<!DOCTYPE html>
<html lang="en">
<head>
<meta charset="utf-8">
<title>Kindred Calm business card</title>
<link rel="stylesheet" href="https://fonts.googleapis.com/css2?family=EB+Garamond:wght@600;700&family=Pinyon+Script&display=swap">
<style>
  :root {
    --backdrop: #dcdcdc;
    --card-white: #ffffff;
    --ink: #2e2e2e;
    --magenta: #b73a82;
    --quote-text: #ffffff;
  }
  * { margin: 0; padding: 0; box-sizing: border-box; }
  html, body {
    width: 1200px;
    height: 1200px;
    overflow: hidden;
    background: var(--backdrop);
  }
  .canvas {
    position: relative;
    width: 1200px;
    height: 1200px;
  }
  .card {
    position: absolute;
    left: 211px;
    width: 762px;
    height: 435px;
  }
  .card--front {
    top: 117px;
    background: var(--card-white);
  }
  .card--back {
    top: 651px;
    background: var(--magenta);
  }
  .brand-name {
    position: absolute;
    top: 140px;
    left: 0;
    width: 100%;
    display: flex;
    justify-content: center;
    align-items: center;
    gap: 12px;
    font-family: "EB Garamond", Georgia, serif;
    font-weight: 600;
    font-size: 40px;
    line-height: 52px;
    color: var(--magenta);
    letter-spacing: 0.5px;
  }
  .brand-dot {
    width: 18px;
    height: 18px;
    border-radius: 50%;
    background: var(--magenta);
  }
  .tagline {
    position: absolute;
    top: 276px;
    left: 0;
    width: 100%;
    text-align: center;
    font-family: "EB Garamond", Georgia, serif;
    font-weight: 700;
    font-size: 46px;
    line-height: 56px;
    color: var(--ink);
    letter-spacing: -0.3px;
    white-space: nowrap;
  }
  .tagline .accent { color: var(--magenta); }
  .quote {
    position: absolute;
    top: 56px;
    left: 0;
    width: 100%;
    text-align: center;
    font-family: "Pinyon Script", cursive;
    font-size: 29px;
    line-height: 45.5px;
    color: var(--quote-text);
    white-space: nowrap;
  }
  .attribution {
    position: absolute;
    top: 346px;
    right: 88px;
    font-family: "Pinyon Script", cursive;
    font-size: 29px;
    line-height: 40px;
    color: var(--quote-text);
  }
</style>
</head>
<body>
<main class="canvas">
  <section class="card card--front">
    <div class="brand-name"><span class="brand-dot"></span>Kindred Calm</div>
    <p class="tagline">sharing <span class="accent">light.</span> a peaceful way of living.</p>
  </section>
  <section class="card card--back">
    <p class="quote">
      "and then it happens... One day you wake up and you're in this place.<br>
      You are in this place where everything is right. Your heart is calm.<br>
      Your soul is lit. Your thoughts are positive. Your vision is clear.<br>
      Your faith is stronger than ever. And you are at peace.<br>
      At peace with where you have been. At peace with what you've been<br>
      through. And at peace with where you're headed."
    </p>
    <p class="attribution">-unknown</p>
  </section>
</main>
</body>
</html>
```